PowerPoint Presentation for Digital Strategy

I have a PPT that needs consistent graphics, images, text clean-up, concise flow, etc.

Larkmoor Strategy is based in Chicago and preparing a presentation to University Bookstores and staff on the benefits of doing an ALL-INclusive model that will lower costs to students.

The pitch includes case studies that show a savings to students on the cost of using digital textbooks over the traditional print textbooks.

Bookstores need to be in the middle of the process and offer course materials included with tuition so that the books will be available on the first day of class. Having the materials shows proof of improved learning outcomes.

Target Market(s)

Universities and University Bookstores

Industry/Entity Type

Education

Requirements
Must have
• Clear, concise flow, charts, images, graphics

```html
<!DOCTYPE html>
<html lang="en">
<head>
<meta charset="utf-8">
<title>From Within Their LMS</title>
<link href="https://fonts.googleapis.com/css2?family=Montserrat:wght@700;800&family=Raleway:ital,wght@0,300;0,400;1,300&display=swap" rel="stylesheet">
<style>
  :root {
    --lime: #9dca3c;
    --white: #ffffff;
    --ink: #3b3a32;
  }
  html, body {
    margin: 0;
    padding: 0;
    overflow: hidden;
    background: var(--lime);
  }
  .slide {
    position: relative;
    width: 1200px;
    height: 675px;
    background: var(--lime);
    overflow: hidden;
    font-family: "Raleway", sans-serif;
  }
  .slide-title {
    position: absolute;
    left: 35px;
    top: 24px;
    margin: 0;
    font-family: "Montserrat", sans-serif;
    font-weight: 800;
    font-size: 74px;
    line-height: 1;
    letter-spacing: 0.5px;
    color: var(--white);
  }
  .slide-subtitle {
    position: absolute;
    left: 37px;
    top: 98px;
    margin: 0;
    font-style: italic;
    font-weight: 300;
    font-size: 40px;
    line-height: 1.1;
    color: var(--white);
  }
  .icon {
    position: absolute;
    fill: var(--ink);
  }
  .icon-search { left: 176px; top: 166px; width: 80px; height: 80px; }
  .icon-laptop { left: 540px; top: 144px; width: 120px; height: 110px; }
  .icon-bulb   { left: 936px; top: 138px; width: 84px;  height: 112px; }
  .benefit {
    position: absolute;
    top: 274px;
    width: 305px;
    height: 345px;
    border: 1.5px solid var(--white);
    box-sizing: border-box;
  }
  .benefit-find   { left: 68px; }
  .benefit-access { left: 446px; }
  .benefit-study  { left: 825px; }
  .benefit-heading {
    position: absolute;
    left: 0;
    right: 0;
    top: 10px;
    margin: 0;
    text-align: center;
    font-weight: 300;
    font-size: 53px;
    line-height: 1;
    color: var(--white);
  }
  .benefit-text {
    position: absolute;
    left: 26px;
    right: 14px;
    margin: 0;
    font-weight: 400;
    font-size: 21px;
    line-height: 26.5px;
    color: var(--ink);
  }
  .benefit-find .benefit-text   { top: 104px; }
  .benefit-access .benefit-text { top: 77px; }
  .benefit-study .benefit-text  { top: 66px; left: 24px; }
</style>
</head>
<body>
<main class="slide">
  <h1 class="slide-title">FROM WITHIN THEIR LMS</h1>
  <p class="slide-subtitle">students can:</p>

  <svg class="icon icon-search" viewBox="0 0 80 80" aria-hidden="true">
    <circle cx="32" cy="32" r="24" fill="none" stroke="#3b3a32" stroke-width="8"/>
    <line x1="50" y1="50" x2="72" y2="72" stroke="#3b3a32" stroke-width="9" stroke-linecap="round"/>
  </svg>

  <svg class="icon icon-laptop" viewBox="0 0 120 110" aria-hidden="true">
    <rect x="10" y="4" width="100" height="70" rx="8" fill="none" stroke="#3b3a32" stroke-width="7"/>
    <path d="M64 30 L64 52 L69 47 L73 56 L76 55 L72 46 L79 46 Z"/>
    <path d="M10 84 L110 84 L118 104 Q118 108 114 108 L6 108 Q2 108 2 104 Z"/>
    <rect x="48" y="100" width="24" height="2" fill="#9dca3c"/>
  </svg>

  <svg class="icon icon-bulb" viewBox="0 0 84 112" aria-hidden="true">
    <rect x="38" y="0" width="7" height="16" rx="3"/>
    <rect x="4" y="20" width="7" height="15" rx="3" transform="rotate(-45 7 27)"/>
    <rect x="73" y="20" width="7" height="15" rx="3" transform="rotate(45 76 27)"/>
    <path d="M42 28 C24 28 12 41 12 57 C12 68 18 75 24 82 L25 88 L59 88 L60 82 C66 75 72 68 72 57 C72 41 60 28 42 28 Z" fill="none" stroke="#3b3a32" stroke-width="7"/>
    <path d="M32 58 L42 68 L52 58 M42 68 L42 86" fill="none" stroke="#3b3a32" stroke-width="6" stroke-linecap="round"/>
    <rect x="26" y="92" width="32" height="6" rx="3"/>
    <rect x="28" y="101" width="28" height="6" rx="3"/>
  </svg>

  <section class="benefit benefit-find">
    <h2 class="benefit-heading">FIND</h2>
    <p class="benefit-text">Each student has single place to easily find their specific digital content for their specific courses and sections</p>
  </section>

  <section class="benefit benefit-access">
    <h2 class="benefit-heading">ACCESS</h2>
    <p class="benefit-text">A single sign-on provides links to adopted content automatically placed on student LMS, eliminating the hassles of navigating access codes and URLs for each and every purchase</p>
  </section>

  <section class="benefit benefit-study">
    <h2 class="benefit-heading">STUDY</h2>
    <p class="benefit-text">Students can focus on using the content for their classes, using the tools to enhance their studying, submit homework or assess their progress…not worrying about whether they have the right content or getting access to it</p>
  </section>
</main>
</body>
</html>
```